Fresh, modern, fun business card for pediatric dental practice

Need a business card for fresh, modern, fun pediatric dental practice

Clean look that matches our website's font and colors

We prefer the look of curved corners on business cards

Target Market(s)

parents (mothers) of young children, professionals, mid-high class

Industry/Entity Type

Dental

Contact Information for Business Card

Maplebrook Pediatric Dentistry
482 Orchard Vale Road
Suite 517
Lindenfield, PA 17990
555.419.3067
www.maplebrookkidsdental.example

Mara Tevlin, DMD
Colette Varnum, DMD
(we are working on our email address, but we would like that on the card as well)

Font styles to use
Sans Serif

Requirements
Must have
• All info; we would also like to make cards for individual staff members
• colors from our website and color palatte, attatched
• use same font and design as website for branding
Nice to have
• clean, simple card that has a pop of color
• we would like to see a few designs with our tag line "Happy visits, healthy teeth"
• we are not sure if we want to have it on there or not
• we would like to see a few designs incorporating the ribbon graphic on our website where the word WELCOME is

```html
<!DOCTYPE html>
<html lang="en">
<head>
<meta charset="utf-8">
<title>Maplebrook Pediatric Dentistry – Business Card</title>
<link rel="stylesheet" href="https://fonts.googleapis.com/css2?family=Open+Sans:wght@400;700&family=Lato:wght@400&display=swap">
<style>
:root{
  --bg:#efe7dc;
  --pink:#ec67a6;
  --magenta:#b02a86;
  --yellow:#fdd82f;
  --gold:#e3aa2a;
  --sun:#f5b41c;
  --band:#f7c64b;
  --plum:#6a3a5e;
  --ribbon:#c7c3c3;
  --ribbon-text:#5b4556;
  --white:#ffffff;
}
*{margin:0;padding:0;box-sizing:border-box}
html,body{width:1200px;height:976px;overflow:hidden;background:var(--bg)}
.canvas{position:relative;width:1200px;height:976px}
.card{position:absolute;width:659px;height:395px;overflow:hidden;box-shadow:0 6px 18px rgba(0,0,0,.18)}
.card--front{left:282px;top:62px;background:var(--yellow)}
.card--back{left:301px;top:535px;background:var(--band)}

.front__top{position:absolute;left:0;top:0;width:100%;height:273px;background:var(--pink)}
.front__name{position:absolute;left:118px;top:200px;width:430px;text-align:center;font:700 66px/1 'Open Sans',sans-serif;color:var(--sun);letter-spacing:1px;white-space:nowrap}
.front__descriptor{position:absolute;left:118px;top:282px;width:430px;text-align:center;font:400 38px/1 'Open Sans',sans-serif;color:var(--magenta);letter-spacing:4.6px;white-space:nowrap}

.back__wave{position:absolute;left:0;top:0;width:659px;height:170px}
.back__logo{position:absolute;left:50px;top:88px;width:174px;text-align:center}
.back__name{font:700 28px/1 'Open Sans',sans-serif;color:var(--sun);letter-spacing:1px;white-space:nowrap}
.back__descriptor{margin-top:6px;font:400 15px/1 'Open Sans',sans-serif;color:var(--magenta);letter-spacing:2.4px;white-space:nowrap}
.back__tagline{position:absolute;left:394px;top:92px;font:400 19px/1 'Lato',sans-serif;color:var(--plum);letter-spacing:-.3px;white-space:nowrap}
.stripe{position:absolute;left:0;width:100%;height:11px;background:var(--pink)}
.stripe--upper{top:161px}
.stripe--lower{top:305px}
.back__panel{position:absolute;left:0;top:172px;width:100%;height:133px;background:var(--gold);color:var(--white);font-family:'Lato',sans-serif}
.back__person{position:absolute;left:0;width:100%;top:22px;text-align:center;font-size:22px;letter-spacing:-.3px}
.contact{position:absolute;display:flex;align-items:center;gap:7px;font-size:13.5px;white-space:nowrap}
.contact svg{width:15px;height:15px}
.contact--phone{left:183px;top:68px}
.contact--email{left:325px;top:68px}
.contact--web{left:227px;top:104px}
.back__address-band{position:absolute;left:0;top:316px;width:100%;height:51px;background:linear-gradient(#e4e4e4,#bdbdbd)}
.ribbon{position:absolute;left:170px;top:321px;width:334px;height:42px}
.ribbon__text{position:absolute;left:170px;top:324px;width:306px;text-align:center;font-family:'Lato',sans-serif;color:var(--ribbon-text);white-space:nowrap}
.ribbon__title{font-size:13.5px;letter-spacing:-.2px}
.ribbon__address{font-size:12.5px;margin-top:2px;letter-spacing:-.2px}
.back__bottom{position:absolute;left:0;top:367px;width:100%;height:28px;background:var(--band)}
</style>
</head>
<body>
<main class="canvas">
  <section class="card card--front" aria-label="Card front">
    <div class="front__top"></div>
    <div class="front__name">maplebrook</div>
    <div class="front__descriptor">pediatric dentistry</div>
  </section>

  <section class="card card--back" aria-label="Card back">
    <svg class="back__wave" viewBox="0 0 659 170" preserveAspectRatio="none">
      <defs>
        <linearGradient id="whiteFade" x1="0" y1="0" x2="0" y2="1">
          <stop offset="0" stop-color="#ffffff"/>
          <stop offset="1" stop-color="#e9e9e9"/>
        </linearGradient>
      </defs>
      <path d="M0 30 Q330 50 659 30 L659 161 L0 161 Z" fill="url(#whiteFade)"/>
    </svg>
    <div class="back__logo">
      <div class="back__name">maplebrook</div>
      <div class="back__descriptor">pediatric dentistry</div>
    </div>
    <div class="back__tagline">Happy visits, healthy teeth</div>
    <div class="stripe stripe--upper"></div>
    <div class="back__panel">
      <div class="back__person">MARA TEVLIN, DMD</div>
      <div class="contact contact--phone">
        <svg viewBox="0 0 16 16" fill="none" stroke="#fff" stroke-width="1.2"><circle cx="8" cy="8" r="7"/><path d="M5.3 4.5l1.4 1.6-.8 1.1c.6 1.2 1.5 2.1 2.7 2.7l1.1-.8 1.6 1.4-.9 1c-2.9-.4-5.6-3.1-6-6z" fill="#fff" stroke="none"/></svg>
        <span>555.419.3067</span>
      </div>
      <div class="contact contact--email">
        <svg viewBox="0 0 16 16" fill="none" stroke="#fff" stroke-width="1.2"><circle cx="8" cy="8" r="7"/><rect x="4.5" y="5.5" width="7" height="5" rx=".6"/><path d="M4.6 5.8L8 8.4l3.4-2.6"/></svg>
        <span>info@maplebrook.example</span>
      </div>
      <div class="contact contact--web">
        <svg viewBox="0 0 16 16" fill="none" stroke="#fff" stroke-width="1.2"><circle cx="8" cy="8" r="7"/><circle cx="8" cy="8" r="3.8"/><path d="M4.2 8h7.6M8 4.2c-1.2 1.2-1.2 6.4 0 7.6M8 4.2c1.2 1.2 1.2 6.4 0 7.6"/></svg>
        <span>www.maplebrookkidsdental.example</span>
      </div>
    </div>
    <div class="stripe stripe--lower"></div>
    <div class="back__address-band"></div>
    <svg class="ribbon" viewBox="0 0 334 42" preserveAspectRatio="none">
      <path d="M0 0 H334 L304 21 L334 42 H0 Z" fill="var(--ribbon)"/>
    </svg>
    <div class="ribbon__text">
      <div class="ribbon__title">MAPLEBROOK PEDIATRIC DENTISTRY</div>
      <div class="ribbon__address">482 Orchard Vale Road Suite 517 Lindenfield, PA 17990</div>
    </div>
    <div class="back__bottom"></div>
  </section>
</main>
</body>
</html>
```